Tarvimoor business cards

Need fresh design for our business cards. Logo must be specific, we are open for everything else.

Contact Information for Business Card

phrase "GMP & JANITORIAL SERVICES" should be used as main point of card

Colors
3176b5
3276b5
85acd3
cedeed
ffffff
0292cd
33a6d7
85cae6
cee9f5

Requirements
Must have
• The logo
Should not have
• crowded designs

```html
<!DOCTYPE html>
<html lang="en">
<head>
<meta charset="utf-8">
<title>Tarvimoor business cards</title>
<link rel="stylesheet" href="https://fonts.googleapis.com/css2?family=Open+Sans:wght@400;600&display=swap">
<style>
  :root {
    --blue-deep: #3176b5;
    --blue-bright: #0292cd;
    --blue-mid: #33a6d7;
    --blue-soft: #85cae6;
    --blue-pale: #cee9f5;
    --ink-grey: #5a5a5a;
    --paper: #ffffff;
    --backdrop: #6f6f6f;
    --logo-blue: #1a78c8;
  }
  * { box-sizing: border-box; margin: 0; padding: 0; }
  html, body {
    width: 1200px; height: 1200px; overflow: hidden;
    background: var(--backdrop);
    font-family: "Open Sans", Arial, sans-serif;
  }
  .sheet {
    position: relative; width: 1200px; height: 1200px;
    display: flex; flex-direction: column; align-items: center; justify-content: center; gap: 54px;
  }
  .card {
    position: relative; width: 880px; height: 503px; overflow: hidden;
    background: var(--paper);
  }
  /* Front side */
  .card-front .accent-bar {
    position: absolute; left: 40px; top: 40px; width: 16px; height: 236px;
    background: var(--blue-deep);
  }
  .contact-block { position: absolute; left: 84px; top: 46px; }
  .person-name { font-size: 34px; font-weight: 600; color: var(--blue-deep); line-height: 1.1; }
  .person-role { font-size: 18px; color: var(--ink-grey); margin: 4px 0 22px; }
  .contact-line {
    display: flex; align-items: flex-start; gap: 10px;
    font-size: 18px; color: var(--ink-grey); line-height: 1.4; margin-bottom: 4px;
  }
  .contact-line svg { flex: none; width: 18px; height: 18px; margin-top: 4px; fill: var(--blue-deep); }
  .contact-gap { height: 16px; }

  .brand-lockup { position: absolute; display: flex; flex-direction: column; align-items: flex-start; }
  .brand-name {
    font-weight: 400; color: var(--logo-blue); letter-spacing: 0.12em; line-height: 1.1;
    display: flex; align-items: center; gap: 14px; text-transform: uppercase;
  }
  .brand-dot { border-radius: 50%; background: var(--logo-blue); }
  .brand-tagline {
    font-weight: 400; color: var(--logo-blue); text-transform: uppercase;
    letter-spacing: 0.28em; white-space: nowrap;
  }
  .card-front .brand-lockup { left: 470px; top: 168px; }
  .card-front .brand-name { font-size: 44px; }
  .card-front .brand-dot { width: 16px; height: 16px; }
  .card-front .brand-tagline { font-size: 13px; margin-top: 6px; }
  .duster-art {
    position: absolute; left: 470px; top: 282px; width: 370px; height: 186px;
    border-radius: 90px 90px 60px 90px;
    background: radial-gradient(ellipse at 45% 60%, var(--blue-bright) 0%, var(--blue-mid) 45%, var(--blue-pale) 100%);
  }
  /* Back side */
  .card-back {
    background: linear-gradient(135deg, #0a7fce 0%, var(--blue-mid) 100%);
  }
  .cloud-art {
    position: absolute; left: 0; top: 70px; width: 700px; height: 433px;
    border-radius: 0 260px 0 0;
    background: linear-gradient(160deg, var(--paper) 0%, #f4f9fd 100%);
  }
  .card-back .brand-lockup { left: 90px; top: 200px; }
  .card-back .brand-name { font-size: 78px; }
  .card-back .brand-dot { width: 26px; height: 26px; }
  .card-back .brand-tagline { font-size: 20px; margin-top: 10px; }
</style>
</head>
<body>
<main class="sheet">
  <section class="card card-front" aria-label="Business card front">
    <div class="accent-bar"></div>
    <div class="contact-block">
      <p class="person-name">Elin Marsh</p>
      <p class="person-role">Creative Designer</p>
      <p class="contact-line">
        <svg viewBox="0 0 24 24"><path d="M12 2a7 7 0 0 0-7 7c0 5 7 13 7 13s7-8 7-13a7 7 0 0 0-7-7zm0 9.5A2.5 2.5 0 1 1 12 6.5a2.5 2.5 0 0 1 0 5z"/></svg>
        <span>Dummy city<br>Dummy Country Land</span>
      </p>
      <div class="contact-gap"></div>
      <p class="contact-line">
        <svg viewBox="0 0 24 24"><path d="M6.6 10.8a15 15 0 0 0 6.6 6.6l2.2-2.2a1 1 0 0 1 1-.25 11.4 11.4 0 0 0 3.6.57 1 1 0 0 1 1 1V20a1 1 0 0 1-1 1A17 17 0 0 1 3 4a1 1 0 0 1 1-1h3.5a1 1 0 0 1 1 1c0 1.25.2 2.45.57 3.57a1 1 0 0 1-.25 1z"/></svg>
        <span>1-555-018273</span>
      </p>
      <p class="contact-line">
        <svg viewBox="0 0 24 24"><path d="M12 2a10 10 0 1 0 0 20 10 10 0 0 0 0-20zm6.9 6h-3a15 15 0 0 0-1.3-3.9A8 8 0 0 1 18.9 8zM12 4c.8 1.2 1.5 2.5 1.9 4h-3.8c.4-1.5 1.1-2.8 1.9-4zM4.3 14a8 8 0 0 1 0-4h3.3a16 16 0 0 0 0 4zm.8 2h3a15 15 0 0 0 1.3 3.9A8 8 0 0 1 5.1 16zm3-8h-3a8 8 0 0 1 4.3-3.9A15 15 0 0 0 8.1 8zM12 20c-.8-1.2-1.5-2.5-1.9-4h3.8c-.4 1.5-1.1 2.8-1.9 4zm2.3-6H9.7a14 14 0 0 1 0-4h4.6a14 14 0 0 1 0 4zm.3 5.9a15 15 0 0 0 1.300-3.9h3a8 8 0 0 1-4.3 3.9zm1.8-5.9a16 16 0 0 0 0-4h3.3a8 8 0 0 1 0 4z"/></svg>
        <span>www.tarvimoor.com</span>
      </p>
      <p class="contact-line">
        <svg viewBox="0 0 24 24"><path d="M3 5h18a1 1 0 0 1 1 1v12a1 1 0 0 1-1 1H3a1 1 0 0 1-1-1V6a1 1 0 0 1 1-1zm1 2.2V17h16V7.2l-8 5.3z"/></svg>
        <span>elin@tarvimoor.com</span>
      </p>
    </div>
    <div class="brand-lockup">
      <p class="brand-name"><span>Tarvimoor</span><span class="brand-dot"></span></p>
      <p class="brand-tagline">GMP &amp; Janitorial Services</p>
    </div>
    <div class="duster-art" role="img" aria-label="Illustration of a feather duster sweeping through a puff of dust clouds with sparkles"></div>
  </section>

  <section class="card card-back" aria-label="Business card back">
    <div class="cloud-art" role="img" aria-label="Large white cloud illustration over the blue background"></div>
    <div class="brand-lockup">
      <p class="brand-name"><span>Tarvimoor</span><span class="brand-dot"></span></p>
      <p class="brand-tagline">GMP &amp; Janitorial Services</p>
    </div>
  </section>
</main>
</body>
</html>
```